Halvern Aid Collective Business Card

I'm in desperate need of some very creative design ideas for a progressive growing long term care business. You can get a pretty good idea of who we are by going to our new website that's about to be launched at halvernaidcollective.net. Halvern Aid Collective merely represents and ties together my two operating companies, Halvern Hearthside and Halvern Elder Residences. I need ideas how to represent this on a small business card and make the name and info legible for a senior patient to read. I'm truly looking forward to seeing what creative ideas come out of this process. I think we will need to have a front and back designed business card to allow for space. I also need to make sure our QR code will fit somewhere as well. I've attached a design of a card that was done, but we're not committed to. Design away!!
I've added the EPS versions of the logos. None of the logos need to include the tagline...."Someone you can depend on", unless you think they should or it should be included in the design elsewhere.
Please ask questions freely. Thank you.
Target Market(s)
Senior market, long term care clients.
Industry/Entity Type
Small Business
Look and feel
Each slider illustrates characteristics of the customer's brand and the style your logo design should communicate.

```html
<!DOCTYPE html>
<html lang="en">
<head>
<meta charset="utf-8">
<title>Halvern Aid Collective – Business Card</title>
<link rel="stylesheet" href="https://fonts.googleapis.com/css2?family=Crimson+Text:wght@400;600&display=swap">
<style>
  :root {
    --bg: #e4e4e4;
    --teal: #78b09b;
    --teal-light: #8cc2ae;
    --teal-text: #5f9c86;
    --charcoal: #545454;
    --ink: #222;
    --white: #ffffff;
  }
  * { margin: 0; padding: 0; box-sizing: border-box; }
  html, body { width: 1200px; height: 872px; overflow: hidden; }
  body {
    background: var(--bg);
    font-family: "Crimson Text", Georgia, serif;
    position: relative;
  }
  .card {
    position: absolute;
    width: 540px;
    height: 310px;
    border-radius: 14px;
    overflow: hidden;
  }
  /* front */
  .card-front { left: 70px; top: 80px; background: var(--white); }
  .card-front .wave { position: absolute; inset: 0; }
  .brand-mark {
    position: absolute;
    left: 118px; top: 40px;
    width: 64px; height: 64px;
    background: var(--teal);
    border-radius: 8px;
  }
  .brand-name {
    position: absolute;
    left: 30px; top: 110px;
    width: 240px;
    text-align: center;
    font-size: 58px;
    line-height: 1;
    color: var(--charcoal);
  }
  .divider {
    position: absolute;
    left: 290px; top: 30px;
    width: 2px; height: 160px;
    background: var(--teal);
  }
  .contact {
    position: absolute;
    left: 306px; top: 30px;
    width: 200px;
    color: var(--ink);
    font-size: 11px;
    line-height: 1.3;
  }
  .contact .person {
    font-size: 14px;
    font-weight: 600;
    letter-spacing: 0.06em;
    color: var(--teal-text);
    text-transform: uppercase;
  }
  .contact .role { font-size: 12px; font-weight: 600; margin-bottom: 20px; }
  .contact .address { margin-bottom: 10px; }
  .contact .line { display: flex; align-items: center; gap: 4px; }
  .contact .icon { width: 9px; height: 9px; fill: var(--charcoal); }
  .contact .web { margin-top: 8px; }
  .contact .web span { color: var(--teal-text); }
  /* back */
  .card-back { left: 590px; top: 500px; background: var(--teal); }
  .card-back .panel {
    position: absolute;
    left: 0; top: 0;
    width: 52%; height: 64%;
    background: var(--teal-light);
    border-bottom-right-radius: 22px;
  }
  .card-back .brand-name-back {
    position: absolute;
    right: 26px; bottom: 38px;
    font-size: 64px;
    line-height: 1;
    color: var(--white);
  }
  /* standalone lockup */
  .lockup {
    position: absolute;
    left: 800px; top: 70px;
    width: 300px;
    text-align: center;
  }
  .lockup .brand-mark-lg {
    width: 62px; height: 62px;
    margin: 0 auto 8px;
    background: var(--teal);
    border-radius: 8px;
  }
  .lockup .brand-name-lg {
    font-size: 64px;
    line-height: 1;
    color: var(--charcoal);
  }
</style>
</head>
<body>

  <section class="card card-front" aria-label="Business card front">
    <svg class="wave" viewBox="0 0 540 310" preserveAspectRatio="none" aria-hidden="true">
      <path d="M0,272 C150,232 290,236 400,218 C470,206 520,180 540,140 L540,310 L0,310 Z" fill="var(--charcoal)"/>
      <path d="M0,292 C150,252 292,256 404,236 C474,222 522,198 540,164 L540,310 L0,310 Z" fill="var(--teal)"/>
    </svg>
    <div class="brand-mark" aria-hidden="true"></div>
    <div class="brand-name">Halvern</div>
    <div class="divider" aria-hidden="true"></div>
    <div class="contact">
      <p class="person">Peter Laine</p>
      <p class="role">Owner</p>
      <p class="address">42 Marrow Lane<br>Brindle, Ontario<br>K0B 1A4</p>
      <p class="line">
        <svg class="icon" viewBox="0 0 10 10" aria-hidden="true"><path d="M1,2 Q1,1 2,1 L3,1 L4,3 L3,4 Q4,6 6,7 L7,6 L9,7 L9,8 Q9,9 8,9 Q1,8 1,2 Z"/></svg>
        555-214-0390
      </p>
      <p class="line">
        <svg class="icon" viewBox="0 0 10 10" aria-hidden="true"><rect x="0.5" y="2" width="9" height="6" rx="1"/><path d="M1,2.5 L5,5.5 L9,2.5" stroke="#fff" stroke-width="0.8" fill="none"/></svg>
        office@halvernaid.ca
      </p>
      <p class="web">www.<span>halvernaidcollective</span>.net</p>
    </div>
  </section>

  <section class="lockup" aria-label="Halvern wordmark">
    <div class="brand-mark-lg" aria-hidden="true"></div>
    <div class="brand-name-lg">Halvern</div>
  </section>

  <section class="card card-back" aria-label="Business card back">
    <div class="panel" aria-hidden="true"></div>
    <div class="brand-name-back">Halvern</div>
  </section>

</body>
</html>
```